Book Cover for Adult Coloring Book

I'd like a unique book cover design for a coloring book we are making for adults. The book cover is for an 8.5"x11" book. I need both the front and back cover created. We will want to include some text about the book on the back cover so there should be room for that. It will be less than 100 words.

1) The title is:

Grown-Up Sketch Pages: Cheeky Remarks Guaranteed To Leave Everyone Snorting Tea

2) A swear word may appear on the cover, however it should similar to some of the examples included.

3) I'd prefer the background be in black or white so that the picture and color "pop" off the page more.

I've included 4 example covers that I really like. Something similar to these is preferred.

Reason: I've had a designer ask if we could extend the deadline. I'd like to get as many options as possible since this is a guaranteed project. Please extend it to Friday, February 19th, 2016. I may choose someone before then, but I'd like to see as many as possible before I do. Thank you, Marcus

Target Market(s)

Adults 25-65

Industry/Entity Type

Publishing Company

Font styles to use
Sans Serif
Decorative
Script

Requirements
Must have
• Unique design and be colorful. It's okay to have a swear word but it should be subtle and similar in design to some of the examples I provided.
Nice to have
• Black or white background that will allow the image/text to "pop" on the page.
Should not have
• No slurs, racial or homophobic words.

```html
<!DOCTYPE html>
<html lang="en">
<head>
<meta charset="utf-8">
<title>Grown-Up Sketch Pages – Cover Wrap</title>
<link rel="stylesheet" href="https://fonts.googleapis.com/css2?family=Emilys+Candy&family=Gochi+Hand&family=Patrick+Hand&display=swap">
<style>
  :root {
    --stage: #ecebe9;
    --paisley-pink: #f4d9dc;
    --paisley-mint: #cdebe5;
    --paisley-cream: #f8f1e4;
    --paisley-peach: #f7dcc6;
    --panel: #ffffff;
    --title-red: #e8432a;
    --ink: #4a4a4a;
    --line: #555555;
    --lime: #b6d72e;
    --green: #7dbb3c;
    --sky: #a9d9e6;
    --orange: #f3a536;
    --khaki: #b5aa96;
    --rust: #c57a3e;
    --purple: #8d5aa6;
    --grey: #a9b0a6;
    --blue: #4a86d6;
    --beige: #e2c9a6;
    --steel: #86acc4;
    --tan: #d9b56a;
    --olive: #6fa444;
    --teal: #4ea2c2;
    --peach: #efcfae;
  }
  * { box-sizing: border-box; margin: 0; padding: 0; }
  html, body { width: 1200px; height: 1200px; overflow: hidden; }
  body { background: var(--stage); position: relative; }

  .cover-wrap {
    position: absolute; left: 30px; top: 250px;
    width: 1140px; height: 700px;
    display: flex;
    box-shadow: 0 6px 24px rgba(0,0,0,.18);
  }
  .back-cover, .spine, .front-cover { position: relative; height: 100%; overflow: hidden; }
  .back-cover { width: 540px; }
  .spine { width: 60px; border-left: 1px solid rgba(0,0,0,.06); border-right: 1px solid rgba(0,0,0,.06); }
  .front-cover { width: 540px; }

  .paisley-pattern {
    position: absolute; inset: 0;
    background:
      radial-gradient(circle at 18% 22%, var(--paisley-mint) 0 7%, transparent 15%),
      radial-gradient(circle at 78% 58%, var(--paisley-mint) 0 6%, transparent 14%),
      radial-gradient(circle at 62% 14%, var(--paisley-pink) 0 6%, transparent 14%),
      radial-gradient(circle at 30% 78%, var(--paisley-peach) 0 6%, transparent 14%),
      radial-gradient(circle at 88% 90%, var(--paisley-pink) 0 5%, transparent 13%),
      linear-gradient(135deg, var(--paisley-pink), var(--paisley-cream) 50%, var(--paisley-pink));
  }

  .clothesline { position: absolute; left: 0; width: 100%; height: 150px; }
  .clothesline svg { position: absolute; inset: 0; width: 100%; height: 100%; }
  .pants-row {
    position: absolute; left: 22px; right: 22px; top: 16px; bottom: 6px;
    border-radius: 4px 4px 14px 14px;
  }
  .row-back-top { background: linear-gradient(90deg, var(--sky) 0 28%, var(--rust) 36% 58%, var(--purple) 66% 88%, var(--sky) 96%); }
  .row-back-bottom { background: linear-gradient(90deg, var(--grey) 0 26%, var(--blue) 34% 56%, var(--beige) 64% 86%, var(--purple) 94%); }
  .row-front-top { background: linear-gradient(90deg, var(--lime) 0 14%, var(--green) 22% 34%, var(--sky) 42% 54%, var(--orange) 62% 76%, var(--khaki) 84%); }
  .row-front-bottom { background: linear-gradient(90deg, var(--steel) 0 14%, var(--tan) 22% 34%, var(--olive) 42% 54%, var(--teal) 62% 76%, var(--peach) 84%); }

  .text-panel { position: absolute; }
  .text-panel svg.panel-shape { position: absolute; inset: 0; width: 100%; height: 100%; }

  .front-title {
    position: absolute; inset: 26px 34px;
    display: flex; flex-direction: column; align-items: center; justify-content: center;
    text-align: center; font-weight: 400;
    font-family: "Emilys Candy", cursive;
    color: var(--title-red);
  }
  .front-title .series { font-size: 26px; line-height: 1.2; }
  .front-title .title-lead { font-size: 50px; line-height: 1.1; }
  .front-title .title-rest { font-size: 36px; line-height: 1.15; }

  .author-tag {
    position: absolute; left: 60px; top: 612px;
    width: 270px; height: 48px; background: var(--panel);
    border-radius: 24px;
    font-family: "Gochi Hand", cursive; color: var(--title-red);
    font-size: 26px; display: flex; align-items: center; justify-content: center;
  }

  .back-content { position: absolute; inset: 34px 44px 28px 48px; }
  .back-heading {
    font-family: "Gochi Hand", cursive; font-weight: 400; color: var(--title-red);
    font-size: 20px; line-height: 1.25; text-align: center;
  }
  .back-heading span { display: block; }
  .back-blurb {
    margin-top: 12px;
    font-family: "Patrick Hand", cursive; color: var(--ink);
    font-size: 19px; line-height: 1.3;
  }

  .spine-title, .spine-author {
    position: absolute; left: 0; width: 100%;
    writing-mode: vertical-rl; font-weight: 400;
    display: flex; align-items: center; justify-content: center;
    font-family: "Gochi Hand", cursive; color: var(--title-red);
  }
  .spine-title { top: 12px; height: 546px; font-size: 14px; white-space: nowrap; }
  .spine-author { top: 566px; height: 124px; font-size: 20px; }
</style>
</head>
<body>
  <div class="cover-wrap">

    <section class="back-cover">
      <div class="paisley-pattern" role="img" aria-label="Soft pastel paisley pattern in pink, mint and cream"></div>

      <div class="clothesline" style="top:70px">
        <svg viewBox="0 0 540 150" preserveAspectRatio="none"><path d="M0 14 Q270 30 540 8" stroke="var(--line)" stroke-width="1.5" fill="none"/></svg>
        <div class="pants-row row-back-top" role="img" aria-label="Illustrated trousers in light blue, brown and purple pegged on a washing line"></div>
      </div>

      <div class="text-panel" style="left:20px; top:232px; width:500px; height:310px">
        <svg class="panel-shape" viewBox="0 0 100 100" preserveAspectRatio="none"><path d="M6 8 Q25 2 45 6 Q70 0 96 5 Q100 30 97 50 Q100 75 94 95 Q70 100 45 94 Q25 99 5 93 Q0 70 3 50 Q0 25 6 8Z" fill="var(--panel)"/></svg>
        <div class="back-content">
          <h2 class="back-heading"><span>Grown-Up Sketch Pages:</span><span>Cheeky Remarks Guaranteed To Leave Everyone Snorting Tea</span></h2>
          <p class="back-blurb">A cheerful stack of pages for grown-ups who need a quiet break and a loud laugh. Each sheet pairs a playful phrase with swirling shapes ready for your pens, pencils and markers. Colour at the kitchen table, on the train or late at night with a cup of tea. Share the giggles, keep the calm, and fill every page your own way.</p>
        </div>
      </div>

      <div class="clothesline" style="top:550px">
        <svg viewBox="0 0 540 150" preserveAspectRatio="none"><path d="M0 10 Q270 2 540 14" stroke="var(--line)" stroke-width="1.5" fill="none"/></svg>
        <div class="pants-row row-back-bottom" role="img" aria-label="Illustrated trousers in grey, blue and beige pegged on a washing line"></div>
      </div>
    </section>

    <section class="spine">
      <div class="paisley-pattern" role="img" aria-label="Soft pastel paisley pattern"></div>
      <h2 class="spine-title">Grown-Up Sketch Pages: Cheeky Remarks Guaranteed To Leave Everyone Snorting Tea</h2>
      <p class="spine-author">Author's name</p>
    </section>

    <section class="front-cover">
      <div class="paisley-pattern" role="img" aria-label="Soft pastel paisley pattern in pink, mint and cream"></div>

      <div class="clothesline" style="top:20px">
        <svg viewBox="0 0 540 150" preserveAspectRatio="none"><path d="M0 18 Q270 6 540 12" stroke="var(--line)" stroke-width="1.5" fill="none"/></svg>
        <div class="pants-row row-front-top" role="img" aria-label="Illustrated trousers in lime, green, light blue, orange and khaki pegged on a washing line"></div>
      </div>

      <div class="text-panel" style="left:30px; top:176px; width:490px; height:290px">
        <svg class="panel-shape" viewBox="0 0 100 100" preserveAspectRatio="none"><path d="M4 14 Q20 4 40 10 Q65 2 95 8 Q100 30 96 48 Q100 70 93 90 Q70 98 50 92 Q25 100 6 94 Q0 75 4 55 Q0 35 4 14Z" fill="var(--panel)"/></svg>
        <h1 class="front-title">
          <span class="series">Grown-Up Sketch Pages:</span>
          <span class="title-lead">Cheeky Remarks</span>
          <span class="title-rest">Guaranteed To Leave</span>
          <span class="title-rest">Everyone Snorting Tea</span>
        </h1>
      </div>

      <div class="clothesline" style="top:455px">
        <svg viewBox="0 0 540 150" preserveAspectRatio="none"><path d="M0 20 Q270 12 540 4" stroke="var(--line)" stroke-width="1.5" fill="none"/></svg>
        <div class="pants-row row-front-bottom" role="img" aria-label="Illustrated trousers in blue, tan, green, teal and beige pegged on a washing line"></div>
      </div>

      <div class="author-tag">Author's name</div>
    </section>

  </div>
</body>
</html>
```